Book writer needs a Book Cover Design for 'Atomic Arms and the Law of States'

A Book Cover Design is required for a new book with a current working title of: 'Atomic Arms and the Law of States' plus subtitle something like: 'from the Harwick Atomic Conflict Panel via the Global Bench of Equity Advisory Opinion to contemporary developments'.

The book will be issued in three formats: hardback, paperback, and electronic.

The Editor of the book is Reginald Palfrey.

The finished size of the paperback front cover will be 15.2mm x 22.9mm. Initial thoughts about themes for the front cover include a nuclear explosion, and perhaps scales of justice, but designers have total freedom to propose ideas.

The back cover will have approximately 250 words of text, and a space at the bottom of about 37mm for publisher logo and ISBN barcode, The designer is free to suggest anything for the back cover.

No illustrations where the copyright is owned by someone else should be used, and the designer must be able to transfer exclusive copyright in the design to the client. The designer will be acknowledged in the book (unless the designer does not want to be).

The themes in the book are:
1. Harwick Atomic conflict Panel
2. Civic Bench Venture
3. Global Bench of Equity Advisory Opinion
4. Dissenting Judgment By Judge Tallisborne
5. Contemporary Activities (e.g. current case involving the Marshall Islands)

Target Market(s)

government decision makers taking decisions about nuclear weapons,iInternational lawyers, students of public international law,

Font styles to use
Serif

Requirements
Must have
• this is in the discretion of the designer
• Title, subtitle, editor (Reginald Palfrey)
Nice to have
• possibly images of nuclear explosion, effects of nuclear weapons, symbols for international law
Should not have
• in the discretion of the designer

```html
<!DOCTYPE html>
<html lang="en">
<head>
<meta charset="utf-8">
<title>Atomic Arms and the Law of States — Cover</title>
<link rel="stylesheet" href="https://fonts.googleapis.com/css2?family=Oswald:wght@400&family=Open+Sans:wght@400&display=swap">
<style>
  :root {
    --ink-black: #0b0707;
    --ember-dark: #241008;
    --band-red: #6e1a12;
    --photo-warm: #8a3a1c;
    --photo-dark: #2a0d08;
    --title-stone: #cfc6b6;
    --emblem-stone: #a39a8a;
    --subtitle-cream: #efe8dc;
    --page-bg: #d8dde1;
  }
  html, body {
    margin: 0;
    padding: 0;
    width: 886px;
    height: 1200px;
    overflow: hidden;
    background: var(--page-bg);
  }
  .cover {
    position: relative;
    width: 886px;
    height: 1200px;
    overflow: hidden;
    background:
      linear-gradient(180deg,
        var(--ink-black) 0%, var(--ink-black) 13%,
        rgba(110,26,18,0.75) 17%, rgba(110,26,18,0.5) 20%, var(--ember-dark) 24%,
        var(--ember-dark) 58%,
        rgba(110,26,18,0.7) 63%, rgba(110,26,18,0.55) 68%,
        var(--ember-dark) 76%, var(--ink-black) 100%);
  }
  .blast-photo {
    position: absolute;
    left: 365px;
    top: 385px;
    width: 280px;
    height: 430px;
    background: radial-gradient(ellipse 60% 55% at 50% 45%, var(--photo-warm) 0%, var(--photo-dark) 100%);
  }
  .title-art {
    position: absolute;
    inset: 0;
    width: 886px;
    height: 1200px;
  }
  .title-line {
    font-family: "Oswald", "Arial Narrow", sans-serif;
    font-weight: 400;
    font-size: 118px;
    fill: var(--title-stone);
    text-transform: uppercase;
  }
  .scales-emblem {
    position: absolute;
    left: 150px;
    top: 948px;
    width: 200px;
    height: 170px;
    background: var(--emblem-stone);
  }
  .subtitle {
    position: absolute;
    left: 374px;
    top: 958px;
    width: 434px;
    margin: 0;
    font-family: "Open Sans", Arial, sans-serif;
    font-size: 21px;
    line-height: 26px;
    color: var(--subtitle-cream);
    text-align: justify;
  }
  .editor {
    position: absolute;
    left: 374px;
    top: 1082px;
    width: 434px;
    margin: 0;
    font-family: "Open Sans", Arial, sans-serif;
    font-size: 21px;
    line-height: 26px;
    color: var(--subtitle-cream);
  }
</style>
</head>
<body>
  <main class="cover">
    <div class="blast-photo" role="img" aria-label="Photograph of a glowing nuclear mushroom cloud rising over a dark horizon"></div>

    <svg class="title-art" viewBox="0 0 886 1200" role="img" aria-label="Atomic Arms and the Law of States">
      <text class="title-line" transform="translate(248 911) rotate(-90)" textLength="822" lengthAdjust="spacing">Atomic Arms</text>
      <text class="title-line" transform="translate(365 911) rotate(-90)" textLength="800" lengthAdjust="spacingAndGlyphs">&amp; the Law of States</text>
    </svg>

    <div class="scales-emblem" role="img" aria-label="Scales of justice emblem"></div>

    <p class="subtitle">from the Harwick Atomic Conflict Panel via the Global Bench of Equity Advisory Opinion to contemporary developments</p>
    <p class="editor">Edited by Reginald Palfrey</p>
  </main>
</body>
</html>
```